Flyer Design Project

We need a flyer and teaser image designed for a March promotional campaign. We have a previous design that just needs a little refresh.
Flyer: the content of the flyer is mostly the same as the pdf you'll see on this link (http://www.quillbrookmedia.com/Digest_Pricing.pdf).
Here are the changes: change June to March, change 2011 to 2012, and remove the address of the bottom. I want the color scheme to be consistent with images I attached called "2011 teaser". I need a pdf file.
Teaser Image: the content of the teaser image is the same as "2011 teaser" image I have attached. All that needs to be changed is the month from "June" to "March". I need this to be a .jpg file that's 600x600 pixels.
Please let me know if you have any questions.
Thanks

```html
<!DOCTYPE html>
<html lang="en">
<head>
<meta charset="utf-8">
<title>Digests – March Pricing</title>
<link rel="stylesheet" href="https://fonts.googleapis.com/css2?family=Titan+One&family=Tinos&display=swap">
<style>
  :root {
    --frame: #3f8196;
    --frame-edge: #2f6a7d;
    --panel-top: #e4f5fb;
    --panel-bottom: #b9d6e2;
    --title-fill: #4a9fb5;
    --title-stroke: #0f2b35;
    --ink: #111111;
    --orange: #f5921f;
    --green: #bccf4e;
    --table-bg: #d8e6ee;
    --art-a: #b0574f;
    --art-b: #d79a4f;
    --art-c: #7a86c6;
  }
  * { margin: 0; padding: 0; box-sizing: border-box; }
  html, body { width: 848px; height: 1200px; overflow: hidden; background: var(--frame); }
  .flyer {
    position: relative; width: 848px; height: 1200px;
    background: linear-gradient(180deg, var(--frame-edge), var(--frame) 50%, var(--frame-edge));
    font-family: "Tinos", "Times New Roman", serif; color: var(--ink);
  }
  .panel {
    position: absolute; left: 21px; top: 21px; width: 806px; height: 1158px;
    background: linear-gradient(180deg, var(--panel-top), var(--panel-bottom));
  }
  .title, .subtitle, .section-title {
    position: absolute; left: 0; width: 848px; text-align: center;
    font-family: "Titan One", "Arial Black", sans-serif;
    color: var(--title-fill);
    -webkit-text-stroke: 2px var(--title-stroke);
    paint-order: stroke fill;
  }
  .title { top: 78px; font-size: 66px; letter-spacing: 2px; -webkit-text-stroke: 3px var(--title-stroke); }
  .subtitle { top: 150px; font-size: 25px; font-style: italic; letter-spacing: 0.5px; }
  .section-title { top: 680px; font-size: 46px; -webkit-text-stroke: 3px var(--title-stroke); }
  .illustration {
    position: absolute; left: 40px; top: 215px; width: 278px; height: 392px;
    background: linear-gradient(180deg, var(--art-a) 0%, var(--art-b) 45%, var(--art-c) 100%);
    border-radius: 14px; opacity: 0.8;
  }
  .details {
    position: absolute; left: 372px; top: 215px; width: 440px;
    font-size: 21px; line-height: 27px;
  }
  .details p { margin-bottom: 27px; }
  .pricing {
    position: absolute; left: 55px; top: 761px; width: 738px; height: 297px;
    background: var(--orange);
  }
  .price-group { position: absolute; top: 0; width: 345px; }
  .price-group.sixteen { left: 9px; }
  .price-group.thirtytwo { left: 381px; }
  .group-label { height: 87px; padding-top: 24px; text-align: center; font-size: 29px; }
  .price-table { background: var(--table-bg); height: 201px; }
  .table-head {
    display: flex; justify-content: space-between; background: var(--green);
    height: 48px; align-items: center; padding: 0 40px 0 12px; font-size: 27px;
  }
  .rows { padding: 6px 0 0 14px; font-size: 27px; line-height: 35px; white-space: nowrap; }
  .footer {
    position: absolute; left: 0; top: 1100px; width: 848px; text-align: center;
    font-size: 16px; line-height: 23px;
  }
</style>
</head>
<body>
<div class="flyer">
  <div class="panel"></div>
  <h1 class="title">DIGESTS</h1>
  <h2 class="subtitle">16 Or 32 pages / 5.5x8.5 Digest</h2>
  <div class="illustration" role="img" aria-label="Illustration of a stack of colourful books with a bookmark"></div>
  <div class="details">
    <p>Submit your art and order by 3:00 pm EST any business day in March to take advantage of this special pricing.</p>
    <p>Each 16 or 32–page digest includes 70# gloss paper throughout, bleeds and saddle–stitching.</p>
    <p>Your directory will be delivered within 12 business days.</p>
    <p>Note: Although your order may deliver sooner, we cannot accept early delivery requests.</p>
  </div>
  <h2 class="section-title">Pricing</h2>
  <div class="pricing">
    <div class="price-group sixteen">
      <div class="group-label">16 Pages</div>
      <div class="price-table">
        <div class="table-head"><span>Quantity</span><span>Price</span></div>
        <div class="rows">
          5,000 ................$1,164.10<br>
          10,000 .............$1,446.40<br>
          15,000 .............$1,803.41<br>
          20,000 .............$2,148.79
        </div>
      </div>
    </div>
    <div class="price-group thirtytwo">
      <div class="group-label">32 Pages</div>
      <div class="price-table">
        <div class="table-head"><span>Quantity</span><span>Price</span></div>
        <div class="rows">
          5,000 ................$1,999.52<br>
          10,000 .............$2,529.50<br>
          15,000 .............$3,173.53<br>
          20,000 .............$3,797.09
        </div>
      </div>
    </div>
  </div>
  <div class="footer">
    800-555-0142 / 317-555-0186 / f 419-555-0173<br>
    www.quillbrookmedia.com
  </div>
</div>
</body>
</html>
```